Interactive Report Dashboard for Data Analytics

Please see this google doc for information and pictures regarding our project.
https://files.brindlework.net/sheet/d/7XpRmTqWz48NvKdLsEj2HbYf90GcAuUo3iZeMkPn/view?share=open
Feel free to message me if you have any questions.
Target Market(s)
This is for video producers, youtubers, and online teachers.
We run focus groups for them and help them understand how their audience reacts to the video content.
Coding
Coded - Design and coding required
Number of Pages Required
5+ page
Colors
Designer to choose colors to be used in the design.
Look and feel
Each slider illustrates characteristics of the customer's brand and the style your logo design should communicate.

```html
<!DOCTYPE html>
<html lang="en">
<head>
<meta charset="utf-8">
<title>Corvale Focus Group – My Summary Reports</title>
<link rel="stylesheet" href="https://fonts.googleapis.com/css2?family=Montserrat:wght@400;500;600;700&display=swap">
<style>
:root{
  --page:#ededed;
  --sidebar:#efefef;
  --white:#ffffff;
  --ink:#222222;
  --muted:#8a8a8a;
  --soft:#9a9a9a;
  --accent:#3d9be9;
  --active-bg:#dfe9f3;
  --band:#d6d6d6;
  --row-tint:#eef6fc;
  --rule:#d5dfe8;
  --footer:#000000;
  --footer-text:#c9c9c9;
  --footer-dim:#6f6f6f;
  --logo:#29a8e0;
  --heart:#f0422b;
  --disgust:#4fb2db;
  --fear:#c055e6;
  --happy:#04e33f;
  --sad:#d45400;
  --anger:#da1f1c;
  --surprise:#f7bc38;
}
*{box-sizing:border-box;margin:0;padding:0}
html,body{width:1200px;height:905px;overflow:hidden}
body{font-family:"Montserrat",sans-serif;background:var(--page);color:var(--ink);position:relative}
.abs{position:absolute}

/* brand lockup */
.brand{display:flex;align-items:center;gap:5px;color:var(--logo);font-weight:600;font-size:12px;white-space:nowrap}
.brand .dot{width:9px;height:9px;border-radius:50%;background:var(--logo)}
.brand-sub{font-size:6px;color:var(--logo);font-weight:600;white-space:nowrap}
.sidebar-brand{left:60px;top:15px}
.sidebar-brand-sub{left:74px;top:30px}
.footer-brand{left:254px;top:658px}
.footer-brand-sub{left:268px;top:673px}

/* sidebar */
.sidebar{left:0;top:0;width:180px;height:592px;background:var(--sidebar);border-right:1px solid #e0e0e0}
.sidebar-top{left:0;top:0;width:180px;height:54px;border-bottom:1px solid #e2e2e2}
.avatar{left:68px;top:66px;width:44px;height:44px;border-radius:50%;background:radial-gradient(circle at 50% 40%,#7a2e1e,#1a1f33)}
.user{left:0;width:180px;top:117px;text-align:center;font-size:9px;color:var(--muted)}
.section-label{left:13px;top:159px;font-size:8.5px;font-weight:500;letter-spacing:.2px}
.nav-item{left:0;width:180px;height:36px;display:flex;align-items:center;font-size:9px;color:var(--soft)}
.nav-item svg{position:absolute;left:7px;width:9px;height:9px}
.nav-item span{position:absolute;left:31px}
.nav-item.active{background:var(--active-bg);color:var(--accent);border-right:2px solid var(--accent)}
.nav-item.large{font-size:10px}
.nav-item .chev{left:auto;right:13px}
.new-campaign{left:0;top:422px;width:180px;height:32px;background:var(--band);color:#fff;font-size:11px;font-weight:600;display:flex;align-items:center;padding-left:16px}
.toggle{left:8px;top:536px;width:34px;height:18px;border-radius:9px;background:#fff}
.toggle i{position:absolute;left:1px;top:1px;width:16px;height:16px;border-radius:50%;background:var(--accent)}
.toggle svg{position:absolute;left:5px;top:5px}

/* header */
.topbar{left:180px;top:0;width:1020px;height:54px;background:#efefef;border-bottom:1px solid #e2e2e2}
.page-title{left:207px;top:17px;font-size:14.5px;font-weight:500;color:#333}
.search{left:696px;top:10px;width:409px;height:32px;background:#dcdcdc;border-radius:3px 0 0 3px;font-size:7.5px;color:#999;display:flex;align-items:center;padding-left:25px}
.search svg{position:absolute;left:10px;top:11px}
.search-btn{left:1105px;top:10px;width:49px;height:32px;background:var(--accent);color:#fff;font-size:8.5px;font-weight:600;display:flex;align-items:center;justify-content:center;border-radius:0 3px 3px 0}
.bell{left:1163px;top:19px}

/* hero panel */
.hero{left:186px;top:60px;width:1014px;height:258px;background:var(--white)}
.hero-title{left:270px;top:180px;font-size:15.5px;font-weight:600}
.filters{left:645px;top:91px;width:477px;height:38px;background:#555}
.chart{left:645px;top:160px}
.tabs{left:206px;top:290px;font-size:8.5px;font-weight:500;color:var(--muted)}
.tab{position:absolute;white-space:nowrap}
.tab.current{color:var(--ink);font-weight:600}
.tab-line{left:492px;top:309px;width:118px;height:2px;background:var(--accent)}

/* question lists */
.q-link{font-size:8.5px;color:var(--muted);font-weight:500;text-align:center;white-space:nowrap}
.q-card{background:#fff;box-shadow:0 4px 8px rgba(0,0,0,.12);display:flex;align-items:center;justify-content:center;font-size:8.5px;font-weight:600;color:var(--ink)}

/* table */
.responses{left:631px;top:326px;width:559px;border-collapse:collapse;font-size:8.5px;table-layout:fixed}
.responses th{background:var(--row-tint);height:19px;font-weight:600;border-right:1px solid #fff}
.responses td{height:52px;vertical-align:top;padding:7px 6px 0;text-align:center;line-height:1.45;border-right:1px solid var(--rule);border-top:1px solid var(--rule)}
.responses tr:nth-child(odd) td{background:var(--row-tint)}
.responses tr:nth-child(even) td{background:#f6f6f6}

/* footer */
.footer{left:0;top:592px;width:1200px;height:313px;background:var(--footer)}
.f-head{font-size:8px;color:var(--footer-text);font-weight:500;letter-spacing:.3px}
.f-link{font-size:7.5px;color:var(--footer-text);white-space:nowrap}
.social{width:15px;height:15px;border-radius:50%;background:#8a8a8a}
.f-rule{left:241px;top:794px;width:719px;height:1px;background:#2d2d2d}
.f-legal{font-size:7.5px;color:var(--footer-dim);white-space:nowrap}
.made{left:566px;top:820px;font-size:9px;font-weight:600;color:#fff;display:flex;gap:6px;align-items:center}
.copy{left:726px;top:824px;font-size:7.5px;color:var(--footer-text);white-space:nowrap}
</style>
</head>
<body>

<!-- Sidebar -->
<aside class="abs sidebar">
  <div class="abs sidebar-top"></div>
  <div class="abs brand sidebar-brand"><span class="dot"></span>Corvale</div>
  <div class="abs brand-sub sidebar-brand-sub">Focus Group</div>
  <div class="abs avatar" role="img" aria-label="Profile photo of the signed-in user"></div>
  <div class="abs user">Dana Whitlow &#x2304;</div>
  <div class="abs section-label">ACCOUNT</div>

  <div class="abs nav-item" style="top:181px"><svg viewBox="0 0 10 10"><path d="M1 5 5 1 9 5V9H6V6H4V9H1Z" fill="#888"/></svg><span>Dashboard</span></div>
  <div class="abs nav-item large" style="top:220px"><svg viewBox="0 0 10 10"><rect x="1" y="2" width="8" height="5" fill="none" stroke="#999"/></svg><span>Messages</span><svg class="chev" viewBox="0 0 10 10"><path d="M2 3 5 6 8 3" fill="none" stroke="#999"/></svg></div>
  <div class="abs nav-item active" style="top:258px"><svg viewBox="0 0 10 10"><path d="M0 5H3L4 2 6 8 7 5H10" fill="none" stroke="#3d9be9"/></svg><span>My Summary Reports</span></div>
  <div class="abs nav-item" style="top:296px"><svg viewBox="0 0 10 10"><circle cx="5" cy="3" r="2" fill="none" stroke="#999"/><path d="M1 9C1 6 9 6 9 9" fill="none" stroke="#999"/></svg><span>Public profile</span></div>
  <div class="abs nav-item" style="top:333px"><svg viewBox="0 0 10 10"><rect x="1" y="2" width="8" height="6" fill="none" stroke="#999"/></svg><span>Plans</span></div>
  <div class="abs nav-item" style="top:372px"><svg viewBox="0 0 10 10"><path d="M5 0 6.5 3.5 10 4 7.2 6.3 8 10 5 8 2 10 2.8 6.3 0 4 3.5 3.5Z" fill="#777"/></svg><span>Affiliate Marketing</span></div>
  <div class="abs new-campaign">+ NEW CAMPAIGN</div>
  <div class="abs nav-item large" style="top:454px"><svg viewBox="0 0 10 10"><circle cx="5" cy="5" r="3" fill="none" stroke="#777" stroke-width="2" stroke-dasharray="2 1"/></svg><span>Settings</span></div>
  <div class="abs nav-item" style="top:492px"><svg viewBox="0 0 10 10"><path d="M7 2A4 4 0 1 0 7 8M5 5H10" fill="none" stroke="#888"/></svg><span>Sign out</span></div>
  <div class="abs toggle"><i></i><svg width="8" height="8" viewBox="0 0 8 8"><path d="M1 1 7 7M7 1 1 7" stroke="#fff" stroke-width="1.2"/></svg></div>
</aside>

<!-- Header -->
<header class="abs topbar"></header>
<h1 class="abs page-title">My Summary Reports</h1>
<div class="abs search"><svg width="9" height="9" viewBox="0 0 10 10"><circle cx="4" cy="4" r="3" fill="none" stroke="#aaa"/><path d="M6.5 6.5 9 9" stroke="#aaa"/></svg>Search...</div>
<div class="abs search-btn">Search</div>
<svg class="abs bell" width="13" height="14" viewBox="0 0 12 13"><path d="M6 1C3.5 1 3 3 3 5V8L1.5 10H10.5L9 8V5C9 3 8.5 1 6 1Z" fill="#666"/><circle cx="6" cy="11.5" r="1.3" fill="#666"/></svg>

<!-- Hero -->
<section class="abs hero"></section>
<h2 class="abs hero-title">All in One Screener for Every Graph</h2>

<svg class="abs filters" viewBox="0 0 477 38">
  <g font-family="Montserrat,sans-serif" font-size="3.5" fill="#ddd">
    <text x="10" y="10">Age</text><text x="4" y="17">Income</text>
  </g>
  <rect x="24" y="6" width="70" height="3" fill="#bcd3f0"/><rect x="31" y="6" width="58" height="3" fill="#3d8fe0"/>
  <rect x="24" y="13" width="80" height="3" fill="#bcd3f0"/><rect x="30" y="13" width="70" height="3" fill="#3d8fe0"/>
  <g fill="#fff"><rect x="10" y="25" width="56" height="5"/><rect x="70" y="25" width="56" height="5"/><rect x="130" y="25" width="56" height="5"/><rect x="190" y="25" width="56" height="5"/><rect x="250" y="25" width="56" height="5"/></g>
  <g fill="#888" font-family="Montserrat,sans-serif" font-size="3"><text x="12" y="29">Gender</text><text x="72" y="29">Region</text><text x="132" y="29">Device</text><text x="192" y="29">Format</text><text x="252" y="29">Language</text></g>
</svg>

<svg class="abs chart" width="477" height="122" viewBox="0 0 477 122" role="img" aria-label="Bar chart of audience emotions">
  <g stroke="#e9e9e9"><line x1="0" y1="6" x2="477" y2="6"/><line x1="0" y1="46" x2="477" y2="46"/><line x1="0" y1="86" x2="477" y2="86"/></g>
  <rect x="14" y="64" width="50" height="56" fill="var(--disgust)"/>
  <rect x="94" y="33" width="50" height="87" fill="var(--fear)"/>
  <rect x="174" y="33" width="50" height="87" fill="var(--happy)"/>
  <rect x="254" y="73" width="50" height="47" fill="var(--sad)"/>
  <rect x="334" y="26" width="50" height="94" fill="var(--anger)"/>
  <rect x="414" y="7" width="50" height="113" fill="var(--surprise)"/>
  <g font-family="Montserrat,sans-serif" font-size="4" fill="#fff" text-anchor="middle">
    <text x="39" y="69">Disgust</text><text x="119" y="38">Fear</text><text x="199" y="38">Happiness</text>
    <text x="279" y="78">Sadness</text><text x="359" y="31">Anger</text><text x="439" y="12">Surprise</text>
  </g>
</svg>

<nav class="abs tabs">
  <span class="tab" style="left:0">Audience Analytic Tools</span>
  <span class="tab" style="left:145px">Real Time Emotion Display</span>
  <span class="tab current" style="left:305px">Survey Responses</span>
</nav>
<div class="abs tab-line"></div>

<!-- Question categories -->
<div class="abs q-link" style="left:214px;width:210px;top:348px">Personality Test Question Responses</div>
<div class="abs q-card" style="left:214px;top:389px;width:209px;height:31px">Demography Question Responses</div>
<div class="abs q-link" style="left:214px;width:210px;top:450px">Political Question Responses</div>
<div class="abs q-link" style="left:214px;width:210px;top:500px">Client's Custom Question Responses</div>

<div class="abs q-card" style="left:463px;top:338px;width:150px;height:31px">Question 1</div>
<div class="abs q-link" style="left:463px;width:150px;top:399px">Question 2</div>
<div class="abs q-link" style="left:463px;width:150px;top:450px">Question 3</div>
<div class="abs q-link" style="left:463px;width:150px;top:500px">Question 4</div>

<!-- Responses table -->
<table class="abs responses">
  <thead><tr><th>Document</th><th>Responses</th><th>Codes</th><th>Comment</th></tr></thead>
  <tbody>
    <tr><td>RESP001</td><td>Lorem ipsum dolor sit amet, consectetur adipiscing elit.</td><td></td><td>Lorem ipsum dolor sit amet, consectetur adipiscing elit.</td></tr>
    <tr><td>RESP002</td><td>Lorem ipsum dolor sit amet, consectetur adipiscing elit.</td><td></td><td>Lorem ipsum dolor sit amet, consectetur adipiscing elit.</td></tr>
    <tr><td>RESP003</td><td>Lorem ipsum dolor sit amet, consectetur adipiscing elit.</td><td></td><td>Lorem ipsum dolor sit amet, consectetur adipiscing elit.</td></tr>
    <tr><td>RESP004</td><td>Lorem ipsum dolor sit amet, consectetur adipiscing elit.</td><td></td><td>Lorem ipsum dolor sit amet, consectetur adipiscing elit.</td></tr>
  </tbody>
</table>

<!-- Footer -->
<footer class="abs footer"></footer>
<div class="abs brand footer-brand"><span class="dot"></span>Corvale</div>
<div class="abs brand-sub footer-brand-sub">Focus Group</div>

<div class="abs f-head" style="left:408px;top:645px">ABOUT</div>
<div class="abs f-link" style="left:408px;top:689px">About Corvale</div>
<div class="abs f-link" style="left:408px;top:707px">Pricing</div>
<div class="abs f-link" style="left:408px;top:726px">Company</div>
<div class="abs f-link" style="left:408px;top:746px">Jobs</div>
<div class="abs f-link" style="left:408px;top:765px">Blog</div>

<div class="abs f-head" style="left:552px;top:645px">SUPPORT</div>
<div class="abs f-link" style="left:552px;top:689px">FAQ</div>
<div class="abs f-link" style="left:552px;top:707px">Help Center</div>
<div class="abs f-link" style="left:552px;top:726px">Terms of Service</div>
<div class="abs f-link" style="left:552px;top:746px">Privacy Policy</div>

<div class="abs f-head" style="left:701px;top:645px">CONTACT</div>
<div class="abs f-link" style="left:701px;top:689px">Email Us</div>
<div class="abs f-link" style="left:701px;top:707px">Live Chat</div>

<div class="abs social" style="left:842px;top:651px"></div>
<div class="abs social" style="left:887px;top:651px"></div>
<div class="abs social" style="left:930px;top:651px"></div>

<div class="abs f-rule"></div>
<div class="abs f-legal" style="left:259px;top:831px">Privacy Policy</div>
<div class="abs f-legal" style="left:335px;top:831px">Terms Of Use</div>
<div class="abs f-legal" style="left:411px;top:831px">Return Policy</div>
<div class="abs made">Made With <svg width="12" height="11" viewBox="0 0 12 11"><path d="M6 11 1 6C-1 3 1 0 3.5 0 5 0 6 1.5 6 1.5S7 0 8.5 0C11 0 13 3 11 6Z" fill="var(--heart)"/></svg></div>
<div class="abs copy">© Corvale. All Rights Reserved.</div>

</body>
</html>
```